Baby Led Weaning App complete design

I want to develop a new app and I need full design for it, including screens, toolbars, icons, images, logo,etc.
The app is aiming to show the User information about baby led weaning, with theory and guidelines and it should also contain a section with recipes for baby lead weaning.

Industry/Entity Type
Baby
Requirements
Must have
- Full design for the app, including screens, toolbars, icons, images, logo,etc.
- The app will be used on smartphones and tablets so design should consider different screen sizes.

Nice to have
- The app is mainly for mums with babys. The design should be bright, happy (positive) and easy to use.
- It would be good to have nice images of babys feeding themselves (no bottle milk). The images in the documents provided need to be replaced.
- Colurs should be gender neutral (not specific to girl or boy).

Should not have
- The should not look too serious or cold.
- Nothing that can be interpreted as negative, heavy, complicated or sad.

```html
<!DOCTYPE html>
<html lang="en">
<head>
<meta charset="utf-8">
<title>Baby Led Weaning – Home</title>
<link rel="stylesheet" href="https://fonts.googleapis.com/css2?family=Roboto:wght@400;500&family=Abril+Fatface&display=swap">
<style>
  :root {
    --page-bg: #efeeef;
    --screen-bg: #eaeaea;
    --card-bg: #f6f6f6;
    --header-pink: #f594c4;
    --text-dark: #1c1c1c;
    --text-body: #5a5a5a;
    --white: #ffffff;
    --badge-green: #2bb24c;
    --icon-blue: #3fb6e0;
    --icon-pink: #ea5aa8;
    --icon-green: #2fc07a;
    --icon-yellow: #e8b62a;
  }
  * { box-sizing: border-box; margin: 0; padding: 0; }
  html, body { width: 1200px; height: 675px; overflow: hidden; }
  body {
    background: var(--page-bg);
    font-family: "Roboto", Arial, sans-serif;
    display: flex; justify-content: center; align-items: center;
  }
  .app-screen {
    width: 372px; height: 640px;
    background: var(--screen-bg);
    border-radius: 18px;
    overflow: hidden;
    box-shadow: 0 10px 30px rgba(0,0,0,0.08);
    display: flex; flex-direction: column;
  }
  .app-header {
    position: relative;
    background: var(--header-pink);
    padding: 14px 16px 18px;
    height: 262px;
  }
  .header-bar {
    display: flex; align-items: center; justify-content: space-between;
    height: 34px;
  }
  .menu-icon, .bell-icon { width: 26px; height: 26px; }
  .app-title {
    color: var(--white);
    font-size: 17px; font-weight: 400; letter-spacing: 0.5px;
  }
  .bell { position: relative; }
  .bell-badge {
    position: absolute; top: -3px; left: -6px;
    width: 13px; height: 13px; border-radius: 50%;
    background: var(--badge-green); color: var(--white);
    font-size: 8px; line-height: 13px; text-align: center; font-weight: 500;
  }
  .feature-banner {
    position: relative;
    margin-top: 12px;
    height: 190px;
    border-radius: 12px;
    overflow: hidden;
    background: linear-gradient(120deg, #f2f5f8 0%, #e9eef2 45%, #f3d8b8 70%, #f7f7f7 100%);
  }
  .feature-title {
    position: absolute; left: 18px; bottom: 22px;
    font-family: "Abril Fatface", Georgia, serif;
    color: var(--text-dark);
    font-size: 22px; line-height: 1.05;
  }
  .feature-title .feature-sub {
    font-family: "Roboto", Arial, sans-serif;
    font-size: 15px; font-weight: 400; font-style: normal;
    display: block; margin-top: 4px; padding-left: 30px;
  }
  .topic-grid {
    flex: 1;
    padding: 8px;
    display: grid;
    grid-template-columns: 1fr 1fr;
    grid-template-rows: 1fr 1fr 1fr;
    gap: 8px;
  }
  .topic-card {
    background: var(--card-bg);
    border-radius: 4px;
    padding: 12px;
    display: flex; align-items: center; gap: 12px;
  }
  .topic-card.wide { grid-column: 1 / 3; }
  .topic-card.stacked { flex-direction: column; align-items: flex-start; gap: 6px; }
  .topic-icon {
    flex: none; width: 52px; height: 52px; border-radius: 50%;
    border: 3px solid currentColor; background: transparent;
  }
  .topic-card.stacked .topic-icon { width: 38px; height: 38px; border-width: 2px; }
  .icon-theory { color: var(--icon-blue); }
  .icon-recipes { color: var(--icon-pink); }
  .icon-start { color: var(--icon-green); }
  .icon-guidelines { color: var(--icon-yellow); }
  .topic-name { font-size: 17px; font-weight: 500; color: var(--text-dark); margin-bottom: 3px; }
  .topic-desc { font-size: 10px; line-height: 1.3; color: var(--text-body); }
</style>
</head>
<body>
  <main class="app-screen">
    <header class="app-header">
      <div class="header-bar">
        <svg class="menu-icon" viewBox="0 0 26 26" aria-label="Menu">
          <g stroke="#fff" stroke-width="2" stroke-linecap="round">
            <line x1="3" y1="7" x2="23" y2="7"/><line x1="3" y1="13" x2="23" y2="13"/><line x1="3" y1="19" x2="23" y2="19"/>
          </g>
        </svg>
        <h1 class="app-title">BABY LED WEANING</h1>
        <div class="bell">
          <svg class="bell-icon" viewBox="0 0 26 26" aria-label="Notifications">
            <path d="M13 4c-4 0-6 3-6 7v5l-2 3h16l-2-3v-5c0-4-2-7-6-7z" fill="#fff"/>
            <circle cx="13" cy="21.5" r="2" fill="#fff"/>
          </svg>
          <span class="bell-badge">2</span>
        </div>
      </div>
      <section class="feature-banner" role="img" aria-label="Photo of a happy baby eating first foods">
        <p class="feature-title">5<br>Best<br>First<br>Foods<span class="feature-sub">for Baby</span></p>
      </section>
    </header>

    <section class="topic-grid">
      <article class="topic-card wide">
        <div class="topic-icon icon-theory" role="img" aria-label="Baby icon"></div>
        <div>
          <h2 class="topic-name">Theory</h2>
          <p class="topic-desc">Lorem ipsum dolor sit amet, consectetur adipisicing elit, sed do eiusmod tempor incididunt</p>
        </div>
      </article>
      <article class="topic-card stacked">
        <div class="topic-icon icon-start" role="img" aria-label="Parent and baby icon"></div>
        <h2 class="topic-name">How to start</h2>
        <p class="topic-desc">Lorem ipsum dolor sit amet, consectetur adipisicing elit,</p>
      </article>
      <article class="topic-card stacked">
        <div class="topic-icon icon-recipes" role="img" aria-label="Plate with spoon and fork icon"></div>
        <h2 class="topic-name">Recipes</h2>
        <p class="topic-desc">Lorem ipsum dolor sit amet, consectetur adipisicing elit,</p>
      </article>
      <article class="topic-card wide">
        <div class="topic-icon icon-guidelines" role="img" aria-label="Swaddled baby icon"></div>
        <div>
          <h2 class="topic-name">Guidelines</h2>
          <p class="topic-desc">Lorem ipsum dolor sit amet, consectetur adipisicing elit, sed do eiusmod</p>
        </div>
      </article>
    </section>
  </main>
</body>
</html>
```